New Business Card Design Project

I would like my card design to look exactly like the logo, design, layout, and print of the current attached file. The only change I would like made would be for the print to say THE KMW GROUP instead of THE HALLORAN GROUP. Basically, just replace his group name with my group name. I would also like the backgroud to be the same texture and color as the attached file. I love the dark blue lettering and house logo on the card.

I am completely open to the rest of the card design. I just want something clean and simple. Only basic contact info required on the card. Maybe just name: Kyle M Warrick and cell # 555.914.2087 and email kyle@orchidhomesagent.com

```html
<!DOCTYPE html>
<html lang="en">
<head>
<meta charset="utf-8">
<title>The KMW Group – Business Card</title>
<link rel="stylesheet" href="https://fonts.googleapis.com/css2?family=Jost:wght@400;500&display=swap">
<style>
  :root {
    --backdrop: #0b0b0b;
    --paper: #e3e3e1;
    --paper-shade: #d6d6d4;
    --ink-navy: #2b3d6b;
    --ink-blue: #2d4f8c;
  }
  * { margin: 0; padding: 0; box-sizing: border-box; }
  html, body {
    width: 1200px;
    height: 1200px;
    overflow: hidden;
    background: var(--backdrop);
  }
  .canvas {
    position: relative;
    width: 1200px;
    height: 1200px;
    display: flex;
    flex-direction: column;
    align-items: center;
    justify-content: center;
    gap: 92px;
  }
  .card {
    position: relative;
    width: 760px;
    height: 434px;
    background: radial-gradient(ellipse at 40% 35%, var(--paper) 0%, var(--paper) 55%, var(--paper-shade) 100%);
    font-family: "Jost", "Futura", sans-serif;
    color: var(--ink-navy);
  }
  .card-front {
    display: flex;
    align-items: center;
    justify-content: center;
  }
  .brand {
    display: flex;
    align-items: center;
    gap: 22px;
  }
  .brand-square {
    width: 70px;
    height: 70px;
    background: var(--ink-blue);
  }
  .brand-name {
    font-size: 30px;
    font-weight: 400;
    letter-spacing: 0.22em;
    line-height: 1.12;
    color: var(--ink-blue);
    text-transform: uppercase;
  }
  .card-back {
    display: flex;
    flex-direction: column;
    align-items: center;
    justify-content: center;
    padding-top: 10px;
  }
  .person-name {
    font-size: 40px;
    font-weight: 400;
    letter-spacing: 0.01em;
    margin-bottom: 38px;
  }
  .contact-list {
    list-style: none;
    display: flex;
    flex-direction: column;
    align-items: center;
    gap: 12px;
    font-size: 23px;
    letter-spacing: 0.02em;
  }
  .contact-item {
    display: flex;
    align-items: center;
    gap: 10px;
  }
  .contact-icon {
    width: 18px;
    height: 18px;
    fill: var(--ink-navy);
  }
</style>
</head>
<body>
  <main class="canvas">
    <section class="card card-front" aria-label="Card front">
      <div class="brand">
        <span class="brand-square" aria-hidden="true"></span>
        <p class="brand-name">The<br>KMW<br>Group</p>
      </div>
    </section>

    <section class="card card-back" aria-label="Card back">
      <h1 class="person-name">Kyle M Warrick</h1>
      <ul class="contact-list">
        <li class="contact-item">
          <svg class="contact-icon" viewBox="0 0 24 24" aria-hidden="true">
            <path d="M6.6 10.8a15.1 15.1 0 0 0 6.6 6.6l2.2-2.2a1 1 0 0 1 1-.25 11.4 11.4 0 0 0 3.6.57 1 1 0 0 1 1 1V20a1 1 0 0 1-1 1A17 17 0 0 1 3 4a1 1 0 0 1 1-1h3.5a1 1 0 0 1 1 1c0 1.25.2 2.45.57 3.6a1 1 0 0 1-.25 1z"/>
          </svg>
          <span>555 914 2087</span>
        </li>
        <li class="contact-item">
          <svg class="contact-icon" viewBox="0 0 24 24" aria-hidden="true">
            <path d="M2 5h20v14H2z M2 5l10 8 10-8" />
          </svg>
          <span>kyle@orchidhomesagent.com</span>
        </li>
      </ul>
    </section>
  </main>
</body>
</html>
```